Window Graphic - Restaurant Interior

We are looking to have designed a Window Graphic created to promote our dinner and pita combos in store. the graphic will be applied to the front side of our counter area glass Dimensions are 18"H x 131" LONG (FRONT) AND THE 2 SIDES ARE 18" H X 16" LONG (LEFT AND RIGHT) - SEE ATTACHED IMAGES OF THE GLASS AREA.

Our 4 Family Combos have also been attached.

PANTONE 306U (BLUE)

Target Market(s)

WOMEN AGES 18-45

Industry/Entity Type

Greek Restaurant

Font styles to use
Serif

Colors
0392cd
0455a3
33a6d7

Requirements
Must have
• Images of Food, The 4 combos, Logo (Brass Lantern)

```html
<!DOCTYPE html>
<html lang="en">
<head>
<meta charset="UTF-8">
<title>Brass Lantern — Family Combos Counter Graphic</title>
<link rel="stylesheet" href="https://fonts.googleapis.com/css2?family=Bebas+Neue&display=swap">
<style>
  :root {
    --blue-deep: #0455a3;
    --blue-mid: #0392cd;
    --blue-light: #33a6d7;
    --cyan-text: #1fb8ec;
    --red: #c4122f;
    --red-dark: #9c0e25;
    --white: #ffffff;
    --page: #eceef1;
  }
  * { margin: 0; padding: 0; box-sizing: border-box; }
  html, body {
    width: 1200px; height: 998px; overflow: hidden;
    background: var(--page);
    font-family: "Bebas Neue", "Oswald", sans-serif;
  }
  .graphic {
    position: absolute; left: 30px; top: 429px;
    width: 1140px; height: 140px;
    display: flex;
    box-shadow: 0 6px 24px rgba(0,0,0,0.12);
  }
  .front-panel {
    position: relative; width: 1016px; height: 140px;
    background: var(--blue-deep);
    overflow: hidden;
  }
  .combo { position: absolute; top: 0; width: 250px; height: 140px; }
  .combo-divider {
    position: absolute; left: -10px; top: 18px;
    width: 2px; height: 96px; background: var(--white); opacity: 0.9;
  }
  .combo-title {
    position: absolute; left: 6px; top: 10px;
    color: var(--cyan-text); font-size: 31px; line-height: 29px;
    letter-spacing: 0.5px;
  }
  .price-tag {
    position: absolute; left: -6px; top: 98px;
    width: 112px; height: 34px;
  }
  .price-tag svg { position: absolute; inset: 0; }
  .price {
    position: absolute; left: 14px; top: 2px;
    color: var(--white); font-size: 32px; line-height: 32px;
  }
  .price sup { font-size: 15px; vertical-align: top; line-height: 18px; margin-left: 1px; }
  .food-photo { position: absolute; left: 86px; top: 8px; width: 124px; height: 124px; }
  .side-panel {
    position: relative; width: 124px; height: 140px;
    background: var(--white); overflow: hidden;
  }
  .side-panel svg { position: absolute; inset: 0; }
  .brand-name {
    position: absolute; left: 34px; top: 42px;
    color: var(--blue-light); font-size: 28px; line-height: 26px;
    letter-spacing: 1px;
  }
</style>
</head>
<body>
  <div class="graphic">
    <div class="front-panel">

      <div class="combo" style="left:22px">
        <div class="combo-title">Pita<br>Combo<br>For 2</div>
        <svg class="food-photo" viewBox="0 0 124 124" role="img" aria-label="Photo of a wrapped chicken pita with lettuce, onion and tzatziki">
          <defs><linearGradient id="g1" x1="0" y1="0" x2="1" y2="1"><stop offset="0" stop-color="#e9c48a"/><stop offset="0.5" stop-color="#8fae4a"/><stop offset="1" stop-color="#d9a56a"/></linearGradient></defs>
          <polygon points="36,3 88,3 121,36 121,88 88,121 36,121 3,88 3,36" fill="url(#g1)" stroke="#fff" stroke-width="5"/>
        </svg>
        <div class="price-tag">
          <svg viewBox="0 0 112 34" preserveAspectRatio="none"><polygon points="0,0 112,0 100,34 0,34" fill="var(--red)"/><polygon points="0,26 12,34 0,34" fill="var(--red-dark)"/></svg>
          <div class="price">$22<sup>95</sup></div>
        </div>
      </div>

      <div class="combo" style="left:272px">
        <div class="combo-divider"></div>
        <div class="combo-title">Pita<br>Combo<br>For 4</div>
        <svg class="food-photo" viewBox="0 0 124 124" role="img" aria-label="Photo of chicken pitas with fries">
          <defs><linearGradient id="g2" x1="0" y1="0" x2="1" y2="1"><stop offset="0" stop-color="#e4b45c"/><stop offset="0.5" stop-color="#d8b98a"/><stop offset="1" stop-color="#9a7a52"/></linearGradient></defs>
          <polygon points="36,3 88,3 121,36 121,88 88,121 36,121 3,88 3,36" fill="url(#g2)" stroke="#fff" stroke-width="5"/>
        </svg>
        <div class="price-tag">
          <svg viewBox="0 0 112 34" preserveAspectRatio="none"><polygon points="0,0 112,0 100,34 0,34" fill="var(--red)"/><polygon points="0,26 12,34 0,34" fill="var(--red-dark)"/></svg>
          <div class="price">$42<sup>95</sup></div>
        </div>
      </div>

      <div class="combo" style="left:522px">
        <div class="combo-divider"></div>
        <div class="combo-title">Dinner<br>Combo<br>For 2</div>
        <svg class="food-photo" viewBox="0 0 124 124" role="img" aria-label="Photo of a Greek salad plate with gyro meat and pita">
          <defs><linearGradient id="g3" x1="0" y1="0" x2="1" y2="1"><stop offset="0" stop-color="#7fa84a"/><stop offset="0.5" stop-color="#e8e2d2"/><stop offset="1" stop-color="#8a5a3c"/></linearGradient></defs>
          <polygon points="36,3 88,3 121,36 121,88 88,121 36,121 3,88 3,36" fill="url(#g3)" stroke="#fff" stroke-width="5"/>
        </svg>
        <div class="price-tag">
          <svg viewBox="0 0 112 34" preserveAspectRatio="none"><polygon points="0,0 112,0 100,34 0,34" fill="var(--red)"/><polygon points="0,26 12,34 0,34" fill="var(--red-dark)"/></svg>
          <div class="price">$26<sup>95</sup></div>
        </div>
      </div>

      <div class="combo" style="left:780px">
        <div class="combo-divider"></div>
        <div class="combo-title">Dinner<br>Combo<br>For 4</div>
        <svg class="food-photo" viewBox="0 0 124 124" role="img" aria-label="Photo of grilled chicken and pepper skewers">
          <defs><linearGradient id="g4" x1="0" y1="0" x2="1" y2="1"><stop offset="0" stop-color="#c44a2a"/><stop offset="0.5" stop-color="#d8a050"/><stop offset="1" stop-color="#5a3a22"/></linearGradient></defs>
          <polygon points="36,3 88,3 121,36 121,88 88,121 36,121 3,88 3,36" fill="url(#g4)" stroke="#fff" stroke-width="5"/>
        </svg>
        <div class="price-tag">
          <svg viewBox="0 0 112 34" preserveAspectRatio="none"><polygon points="0,0 112,0 100,34 0,34" fill="var(--red)"/><polygon points="0,26 12,34 0,34" fill="var(--red-dark)"/></svg>
          <div class="price">$52<sup>95</sup></div>
        </div>
      </div>

    </div>

    <div class="side-panel">
      <svg viewBox="0 0 124 140" preserveAspectRatio="none">
        <path d="M0,0 L20,0 C4,30 6,70 26,100 C38,118 50,130 56,140 L0,140 Z" fill="var(--blue-deep)"/>
        <path d="M20,0 C4,30 6,70 26,100 C38,118 50,130 56,140" fill="none" stroke="var(--blue-light)" stroke-width="3"/>
      </svg>
      <div class="brand-name">Brass<br>Lantern</div>
    </div>
  </div>
</body>
</html>
```